Geschäftspapiere für Zimmerei
Zielgruppe
Zimmerei Holzbau
Aufgabenstellung
Das Logo
Gerold Wenck
Lindenweg 42
87634 Sonthofen
ein Wasserzeichen oder eine dezente Zeichnung mit einbringen währe schön

```html
<!DOCTYPE html>
<html lang="de">
<head>
<meta charset="utf-8">
<title>Zimmerei Wenck – Briefbogen</title>
<link href="https://fonts.googleapis.com/css2?family=Open+Sans:wght@400;600;700&family=Arimo:wght@400&display=swap" rel="stylesheet">
<style>
  :root {
    --bg: #e4e5e6;
    --paper: #ffffff;
    --red: #ee1c1c;
    --graphite: #4a4f52;
    --green: #1f6b3b;
    --ink: #2b2b2b;
    --muted: #555;
    --watermark: #efefef;
  }
  * { box-sizing: border-box; margin: 0; padding: 0; }
  html, body { width: 1200px; height: 945px; overflow: hidden; background: var(--bg); }
  .letterhead {
    position: absolute; left: 282px; top: 22px;
    width: 636px; height: 900px;
    background: var(--paper);
    box-shadow: 0 4px 18px rgba(0,0,0,.18);
    overflow: hidden;
    font-family: "Open Sans", sans-serif;
    color: var(--ink);
  }
  .top-rule { position: absolute; left: 0; top: 0; width: 100%; height: 4px; background: var(--red); }
  .brand {
    position: absolute; left: 52px; top: 70px;
    display: flex; align-items: center; gap: 10px;
    font-weight: 700; font-size: 24px; color: var(--green); letter-spacing: .5px;
    white-space: nowrap;
  }
  .brand-dot { width: 16px; height: 16px; border-radius: 50%; background: var(--green); }
  .sender-line {
    position: absolute; left: 52px; top: 128px;
    font-size: 6.5px; color: var(--muted); white-space: nowrap;
    border-bottom: .7px solid var(--muted); padding-bottom: 2px;
  }
  .sender-line .sep { color: var(--red); padding: 0 2px; }
  .contact {
    position: absolute; left: 392px; top: 34px;
    border-left: .8px solid #333; padding-left: 10px;
    font-size: 7px; line-height: 10.5px; color: var(--ink); font-style: normal;
    white-space: nowrap;
  }
  .contact-row { display: flex; align-items: center; gap: 5px; }
  .contact-row svg { width: 7px; height: 7px; fill: var(--red); flex: none; }
  .contact-address { padding-left: 2px; }
  .watermark {
    position: absolute; left: 250px; top: 640px;
    font-weight: 700; font-size: 36px; color: var(--watermark);
    display: flex; align-items: center; gap: 14px; letter-spacing: 1px;
    white-space: nowrap;
  }
  .watermark-square { width: 34px; height: 34px; background: var(--watermark); }
  .letter {
    position: absolute; left: 86px; top: 300px; width: 440px;
    font-family: "Arimo", sans-serif; font-size: 10.5px; line-height: 12.5px; color: var(--ink);
  }
  .salutation { margin-bottom: 6px; }
  .letter p { margin-bottom: 12px; }
  .signature {
    margin-top: 10px; width: 150px; height: 44px;
    background: linear-gradient(90deg, #f4f4f4, #e9e9e9);
    border-radius: 4px;
  }
  .fold-mark { position: absolute; left: 0; width: 14px; height: .6px; background: #aaa; }
  .footer-art { position: absolute; left: 0; top: 0; }
  .footer-info {
    position: absolute; left: 70px; top: 770px;
    display: flex; gap: 12px; font-size: 7.5px; line-height: 10px; color: var(--ink);
    white-space: nowrap;
  }
  .footer-col { padding-right: 12px; border-right: .8px solid #333; }
  .footer-col:last-child { border-right: 0; }
  .website {
    position: absolute; right: 22px; top: 836px;
    font-size: 9px; color: #fff; letter-spacing: .5px;
  }
</style>
</head>
<body>
  <main class="letterhead">
    <div class="top-rule"></div>

    <div class="brand"><span class="brand-dot"></span>Zimmerei Wenck</div>
    <div class="sender-line">Wenck GmbH &amp; Co. KG<span class="sep">|</span>Lindenweg 42<span class="sep">|</span>D-87634 Kaltbrunn</div>

    <address class="contact">
      <div class="contact-address">Wenck GmbH &amp; Co. KG<br>Lindenweg 42<br>D-87634 Kaltbrunn</div>
      <div class="contact-row"><svg viewBox="0 0 24 24"><path d="M6.6 10.8a15 15 0 006.6 6.6l2.2-2.2c.3-.3.7-.4 1-.2 1.1.4 2.3.6 3.6.6.6 0 1 .4 1 1V20c0 .6-.4 1-1 1A17 17 0 013 4c0-.6.4-1 1-1h3.5c.6 0 1 .4 1 1 0 1.3.2 2.5.6 3.6.1.3 0 .7-.2 1z"/></svg>+49 7364 55120-0</div>
      <div class="contact-row"><svg viewBox="0 0 24 24"><path d="M6.6 10.8a15 15 0 006.6 6.6l2.2-2.2c.3-.3.7-.4 1-.2 1.1.4 2.3.6 3.6.6.6 0 1 .4 1 1V20c0 .6-.4 1-1 1A17 17 0 013 4c0-.6.4-1 1-1h3.5c.6 0 1 .4 1 1 0 1.3.2 2.5.6 3.6.1.3 0 .7-.2 1z"/></svg>+49 176 40218835 (Gerold Wenck)</div>
      <div class="contact-row"><svg viewBox="0 0 24 24"><path d="M6.6 10.8a15 15 0 006.6 6.6l2.2-2.2c.3-.3.7-.4 1-.2 1.1.4 2.3.6 3.6.6.6 0 1 .4 1 1V20c0 .6-.4 1-1 1A17 17 0 013 4c0-.6.4-1 1-1h3.5c.6 0 1 .4 1 1 0 1.3.2 2.5.6 3.6.1.3 0 .7-.2 1z"/></svg>+49 152 61937402 (Anton Wenck)</div>
      <div class="contact-row"><svg viewBox="0 0 24 24"><path d="M2 5h20v14H2z M2 5l10 8 10-8"/></svg>gerold@zimmerei-wenck.de</div>
    </address>

    <div class="watermark" aria-hidden="true"><span class="watermark-square"></span>Zimmerei Wenck</div>

    <span class="fold-mark" style="top:300px"></span>
    <span class="fold-mark" style="top:450px"></span>
    <span class="fold-mark" style="top:600px"></span>

    <section class="letter">
      <div class="salutation">Herr Lorenz</div>
      <p>Lorem ipsum dolor sit amet, consectetur adipiscing elit. Proin tincidunt, lectus id malesuada cursus, lorem augue egestas magna, ut mattis orci ante ut arcu. Sed mauris tellus, fermentum quis ligula nec, posuere pulvinar eros. Nam at mi quis velit pellentesque finibus. Donec lacus velit, faucibus mollis dolor nec, finibus pellentesque orci. Duis sed dictum elit, ut posuere arcu. Phasellus ac dolor et ante consequat rutrum nec nec tortor. Donec consequat, nibh sit amet pulvinar faucibus, turpis magna venenatis diam, vel pretium eros erat vestibulum nulla.</p>
      <p>Sed pretium ac enim eu viverra. Aliquam ac est eget magna convallis convallis. Aenean augue purus, finibus eget turpis quis, finibus dignissim nibh. Phasellus viverra lobortis dignissim. Duis varius turpis in sapien accumsan facilisis. Sed vehicula gravida diam a interdum. Nullam convallis ligula id erat egestas consequat. Integer consectetur ex vel aliquet iaculis. Vestibulum molestie sodales mauris, at tincidunt risus pellentesqu.</p>
      <p>Mauris facilisis, lectus at accumsan tincidunt, dui magna imperdiet sem, quis tempor est lectus eu ipsum. Praesent in fermentum nisl. Maecenas at lorem at odio interdum iaculis. Pellentesque cursus nulla nunc, ut suscipit nulla maximus et. Donec maximus rhoncus metus, vel laoreet nisi pretium sit amet. Donec posuere enim lectus, vitae aliquam augue tincidunt dignissim. Morbi vitae congue velit, quis elementum.</p>
      <div class="signature" role="img" aria-label="Handschriftliche Unterschrift von Gerold Wenck"></div>
    </section>

    <svg class="footer-art" width="636" height="900" viewBox="0 0 636 900" aria-hidden="true">
      <path d="M220 872 C400 850 520 800 636 735 L636 760 C520 815 400 855 220 872 Z" fill="var(--graphite)"/>
      <path d="M0 880 C250 876 460 830 636 758 L636 900 L0 900 Z" fill="var(--red)"/>
    </svg>

    <footer class="footer-info">
      <div class="footer-col">Bankverbindung:<br>Bank: Talbank Oberau eG</div>
      <div class="footer-col">SteuerID: DE418260955<br>Umsatzsteuer ID: 62 104 377 019</div>
      <div class="footer-col">BIC: TALBDEM1XXX<br>IBAN: DE21 7305 0011 0482 3316 90</div>
    </footer>
    <div class="website">www.zimmerei-wenck.de</div>
  </main>
</body>
</html>
```